Gather the Marrow Book Cover

Looking for a cover for my book, Gather the Marrow. Part memoir, part self help - this book is one woman's journey breaking free of the patriarchy and stepping into her divine purpose. Think "boss ass bitch" in NYC transitions to Spiritual Goddess to the beaches of Costa Rica. We are playing on the archetypes of Wounded Masculine to Divine Feminine. Breaking the mold of being a good girl and owning her wild.

Target Market(s)

25-35 yr old female

Industry/Entity Type

Personal Development, Memoir

Other font styles liked:
• Pink #ff0099 Yellow #ffdf2b Teal #1fc4cd Gather - Brittany The - open sans Marrow - Bebas Neue

Colors
FFF300
FFF600
FEFA6F
FFFEC7
FFFEE8
E54698
E96AAD
F1A4CE
F9D9EA
FCEFF6

Requirements
Nice to have

```html
<!DOCTYPE html>
<html lang="en">
<head>
<meta charset="utf-8">
<title>Gather the Marrow — Book Cover</title>
<link rel="stylesheet" href="https://fonts.googleapis.com/css2?family=Bebas+Neue&family=Great+Vibes&family=Roboto+Condensed:wght@400&display=swap">
<style>
  :root {
    --cover-pink: #f9d7e8;
    --title-pink: #e8078b;
    --frame-yellow: #ffed1f;
    --foliage-deep: #4d5d73;
    --foliage-soft: #8a9bb0;
  }
  html, body {
    margin: 0;
    padding: 0;
    width: 812px;
    height: 1200px;
    overflow: hidden;
    background: var(--cover-pink);
  }
  .cover {
    position: relative;
    width: 812px;
    height: 1200px;
    background: var(--cover-pink);
    overflow: hidden;
  }
  .foliage {
    position: absolute;
    display: block;
    z-index: 0;
  }
  .foliage--top-left { left: 24px; top: 38px; width: 272px; height: 412px; }
  .foliage--bottom-right { left: 560px; top: 560px; width: 232px; height: 248px; }
  .title-frame {
    position: absolute;
    z-index: 1;
    left: 153px;
    top: 194px;
    width: 515px;
    height: 507px;
    border: 9px solid var(--frame-yellow);
    box-shadow: 2px 3px 6px rgba(120, 70, 90, 0.35), inset 1px 2px 4px rgba(120, 70, 90, 0.25);
  }
  .title-main,
  .title-joiner,
  .title-accent,
  .genre-label,
  .author-name {
    position: absolute;
    z-index: 2;
    margin: 0;
  }
  .title-main {
    left: 162px;
    top: 200px;
    font-family: "Great Vibes", cursive;
    font-weight: 400;
    font-size: 220px;
    line-height: 1;
    color: var(--title-pink);
    white-space: nowrap;
  }
  .title-joiner {
    left: 588px;
    top: 388px;
    font-family: "Roboto Condensed", sans-serif;
    font-size: 64px;
    line-height: 1;
    color: var(--title-pink);
  }
  .title-accent {
    left: 176px;
    top: 470px;
    width: 490px;
    text-align: center;
    font-family: "Bebas Neue", sans-serif;
    font-size: 158px;
    line-height: 1;
    letter-spacing: 4px;
    color: var(--frame-yellow);
    text-shadow: 2px 3px 3px rgba(120, 70, 90, 0.35);
  }
  .genre-label {
    left: 153px;
    top: 645px;
    width: 534px;
    text-align: center;
    font-family: "Roboto Condensed", sans-serif;
    font-size: 32px;
    line-height: 1;
    color: var(--title-pink);
  }
  .author-name {
    left: 0;
    top: 990px;
    width: 812px;
    text-align: center;
    font-family: "Great Vibes", cursive;
    font-size: 86px;
    line-height: 1;
    color: var(--title-pink);
  }
</style>
</head>
<body>
  <main class="cover">
    <svg class="foliage foliage--top-left" viewBox="0 0 272 412" role="img" aria-label="Botanical illustration of slate-blue leaves with small white and cream blossoms and pine sprigs">
      <defs>
        <radialGradient id="foliage-tl" cx="50%" cy="45%" r="50%">
          <stop offset="0%" stop-color="#4d5d73" stop-opacity="0.75"/>
          <stop offset="65%" stop-color="#8a9bb0" stop-opacity="0.45"/>
          <stop offset="100%" stop-color="#8a9bb0" stop-opacity="0"/>
        </radialGradient>
      </defs>
      <ellipse cx="136" cy="206" rx="134" ry="204" fill="url(#foliage-tl)"/>
    </svg>

    <svg class="foliage foliage--bottom-right" viewBox="0 0 232 248" role="img" aria-label="Botanical illustration of slate-blue leaves with small white and cream blossoms and pine sprigs">
      <defs>
        <radialGradient id="foliage-br" cx="55%" cy="55%" r="50%">
          <stop offset="0%" stop-color="#4d5d73" stop-opacity="0.7"/>
          <stop offset="65%" stop-color="#8a9bb0" stop-opacity="0.4"/>
          <stop offset="100%" stop-color="#8a9bb0" stop-opacity="0"/>
        </radialGradient>
      </defs>
      <ellipse cx="120" cy="126" rx="112" ry="120" fill="url(#foliage-br)"/>
    </svg>

    <div class="title-frame"></div>

    <h1 class="title-main">Gather</h1>
    <div class="title-joiner">the</div>
    <div class="title-accent">MARROW</div>
    <div class="genre-label">a memoir</div>

    <div class="author-name">Delia Varonne</div>
  </main>
</body>
</html>
```